Website design for labour force (commercial truck driver) company

Looking for a Wordpress template (or design files in conjunction with a free Wordpress template).
Company tag line:
CargoLoop – On Demand, Professional Drivers
Real Drivers | Real Standards | Real Results
Logo design has already been completed and is attached

Company provides contract drivers to trucking companies. Pinnacle market is both the trucking companies looking for drivers and drivers looking for work.
Design to encompass header / footer and basic page design, navigation menu, home page, contact page. Customer will add content and additional pages over time.

```html
<!DOCTYPE html>
<html lang="en">
<head>
<meta charset="utf-8">
<title>CargoLoop – On Demand, Professional Drivers</title>
<link href="https://fonts.googleapis.com/css2?family=Oswald:wght@400;500;600&family=Urbanist:wght@400;500;600;700&display=swap" rel="stylesheet">
<style>
:root{
  --green:#0f7a57;
  --green-dark:#0b5f44;
  --green-soft:#e3f1eb;
  --ink:#1c1f22;
  --muted:#6b7278;
  --line:#e3e6e8;
  --panel:#f1f2f3;
  --white:#ffffff;
}
*{margin:0;padding:0;box-sizing:border-box}
html,body{width:1200px;height:5376px;overflow:hidden;background:var(--white)}
body{font-family:"Urbanist",sans-serif;color:var(--ink);position:relative}
.abs{position:absolute}
h1,h2,h3{font-family:"Oswald",sans-serif;font-weight:400;line-height:1.1}
.eyebrow{font-size:14px;color:var(--green);font-weight:500}
.para{font-size:11.5px;line-height:22px;color:var(--muted)}
.btn{display:inline-flex;align-items:center;gap:12px;background:var(--green);color:var(--white);border-radius:20px;padding:4px 5px 4px 14px;font-size:11px;font-weight:500;height:32px}
.btn .arrow{width:24px;height:24px;border-radius:50%;background:var(--white);display:flex;align-items:center;justify-content:center}
.ticks li{list-style:none;display:flex;align-items:center;gap:10px}
.photo{border-radius:14px}
.logo{display:flex;align-items:center;gap:9px;font-family:"Urbanist",sans-serif;font-weight:700;color:var(--white)}
.logo .dot{width:28px;height:28px;border-radius:50%;background:var(--white)}

/* header + hero */
.hero{top:0;left:0;width:1200px;height:606px;background:linear-gradient(100deg,#1d2b22 0%,#3b4d3a 35%,#2f6e66 60%,#1f3a33 85%,#26352c 100%)}
.topbar{top:10px;left:150px;width:900px;display:flex;justify-content:space-between;font-size:9px;color:var(--white)}
.topbar .soc{display:inline-flex;gap:6px;margin-left:8px;vertical-align:middle}
.topbar .soc i{width:9px;height:9px;border-radius:50%;background:var(--white);display:inline-block}
.nav{top:46px;left:150px;width:900px;display:flex;align-items:center;justify-content:space-between}
.nav .logo{font-size:21px}
.menu{display:flex;gap:34px;font-size:10.5px;color:var(--white);margin-left:150px}
.nav .btn{height:34px}
.hero-title{top:140px;left:150px;color:var(--white)}
.hero-title .l1{font-family:"Oswald",sans-serif;font-weight:600;font-size:80px;line-height:84px;letter-spacing:1px}
.hero-title .l2{font-family:"Oswald",sans-serif;font-weight:500;font-size:46px;line-height:52px}
.hero-title .l3{font-family:"Oswald",sans-serif;font-weight:600;font-size:68px;line-height:76px}
.search{top:386px;left:150px;width:326px;height:38px;border-radius:20px;background:rgba(255,255,255,.18);border:1px solid rgba(255,255,255,.35);display:flex;align-items:center;justify-content:space-between;padding:0 6px 0 16px;color:var(--white);font-size:11px}
.search .go{width:26px;height:26px;border-radius:50%;background:var(--white);display:flex;align-items:center;justify-content:center}
.find{top:452px;left:150px}
.rating{top:450px;left:292px;display:flex;align-items:center;gap:8px;color:var(--white)}
.rating .name{font-size:26px;font-weight:600}
.rating small{font-size:9px;display:block}
.rating .stars{color:#f4c430;font-size:9px;letter-spacing:1px}
.hero-card{top:440px;left:862px;width:188px;height:144px;border-radius:10px;background:rgba(255,255,255,.14);border:1px solid rgba(255,255,255,.3);padding:10px;color:var(--white);font-size:8.5px}
.hero-card .row{border-bottom:1px solid rgba(255,255,255,.3);padding:6px 0;display:flex;justify-content:space-between}
.hero-card p{font-size:7px;line-height:11px;opacity:.85;margin-top:6px}

/* about */
.about-photo{top:672px;left:182px;width:388px;height:440px;background:linear-gradient(160deg,#c9d6e2,#6d86a0 50%,#3c4a55)}
.badge{top:845px;left:150px;width:96px;height:94px;background:var(--green);border-radius:8px;color:var(--white);padding:14px 10px}
.badge b{font-family:"Oswald",sans-serif;font-size:38px;font-weight:500;display:block;line-height:40px}
.badge span{font-size:10px}
.about-text{top:686px;left:622px;width:430px}
.about-text h2{font-size:44px;margin:10px 0 24px}
.about-text .ticks{margin:22px 0 38px;font-size:11px;display:grid;gap:12px}

/* go-to */
.goto{top:1228px;left:150px;width:420px}
.goto h2{font-size:44px;margin-bottom:50px}
.goto .btn{margin-top:44px}
.goto-photo{top:1215px;left:611px;width:439px;height:448px;background:linear-gradient(150deg,#e8edf0,#b8c4cc 50%,#7c8f98)}
.driver-card{top:1242px;left:636px;width:199px;height:177px;background:var(--white);border-radius:10px;padding:14px;font-size:10px;box-shadow:0 4px 14px rgba(0,0,0,.08)}
.driver-card .who{display:flex;align-items:center;gap:8px;font-size:13px;font-weight:600;margin-bottom:10px}
.driver-card .who i{width:24px;height:24px;border-radius:50%;background:#4b5a63}
.driver-card p{color:var(--muted);line-height:17px}
.driver-card small{font-size:7.5px;color:var(--muted);line-height:12px;display:block}

.stats{top:1732px;left:150px;width:900px;display:flex;justify-content:space-between}
.stat{display:flex;gap:14px;align-items:center}
.stat b{font-family:"Oswald",sans-serif;font-weight:400;font-size:42px}
.stat span{font-size:10.5px;line-height:20px;width:160px}

.trucks{top:1836px;left:0;width:1200px;height:407px;background:linear-gradient(180deg,#f4f5f6 0%,#b7bfc4 40%,#4a5258 75%,#c9cdd0 100%)}

/* why */
.why-photo{top:2337px;left:150px;width:424px;height:439px;border-radius:6px;background:linear-gradient(180deg,#bcd2e6,#eef3f6 55%,#8a9399)}
.why-box{top:2337px;left:609px;width:441px;height:439px;background:var(--panel);border-radius:6px;padding:36px 28px}
.why-box h2{font-size:40px;margin-bottom:26px}
.why-box .ticks{font-size:17px;display:grid;gap:20px}
.why-box .btns{display:flex;gap:14px;margin-top:40px}

/* how */
.how-head{top:2878px;left:0;width:1200px;text-align:center}
.how-head h2{font-size:42px;margin-top:10px}
.step{width:300px;text-align:center;top:3000px}
.step .circ{width:166px;height:166px;border-radius:50%;margin:0 auto;border:4px solid var(--white);box-shadow:0 0 0 1px var(--line)}
.step h3{font-family:"Urbanist",sans-serif;font-size:14px;font-weight:600;margin-top:22px;line-height:22px}
.step p{font-size:11px;line-height:24px;color:var(--muted);margin:8px auto 0;width:220px}

/* cta */
.cta{top:3433px;left:150px;width:894px;height:251px;background:var(--green);border-radius:14px}
.cta h2{top:3490px;left:176px;font-size:44px;color:var(--white)}
.cta-btns{top:3592px;left:176px;display:flex;gap:16px}
.cta-btns .btn{background:transparent;border:1px solid var(--white)}
.cta-truck{top:3381px;left:595px;width:490px;height:344px;border-radius:10px 60px 10px 10px;background:linear-gradient(120deg,#dfe4e8 0%,#c3cbd1 50%,#1d8a62 70%,#11593f 100%)}

/* testimonial */
.testi-head{top:3800px;left:0;width:1200px;text-align:center;font-size:44px}
.avatar{top:3903px;left:158px;width:134px;height:134px;border-radius:50%;background:radial-gradient(circle,#e28a3c 0%,#5e6b4d 70%)}
.testi-text{top:3917px;left:334px;width:720px;font-size:13px;line-height:30px;color:var(--muted)}
.testi-name{top:4112px;left:150px;font-size:14px;line-height:26px}
.arrows{top:4114px;left:955px;display:flex;gap:14px}
.arrows span{width:40px;height:40px;border-radius:50%;border:1.5px solid var(--ink);display:flex;align-items:center;justify-content:center}
.brands{top:4212px;left:52px;width:1096px;display:flex;justify-content:space-between;align-items:center;font-size:32px;font-weight:600;color:#111}
.brands span{display:flex;align-items:center;gap:8px}
.brands i{width:22px;height:22px;border-radius:50%;background:#111}

/* contact */
.map{top:4383px;left:0;width:595px;height:522px;background:radial-gradient(ellipse at 40% 50%,#eceeef 0%,#f7f8f8 70%,#fff 100%)}
.pin{width:22px;height:28px}
.contact{top:4351px;left:595px;width:484px;height:585px;background:var(--white);border-radius:10px;box-shadow:0 4px 24px rgba(0,0,0,.09);padding:56px 30px 0}
.contact h2{font-size:42px;margin-bottom:16px}
.contact .info{font-size:11px;display:grid;gap:14px;margin-bottom:30px}
.contact .info div{display:flex;align-items:center;gap:10px}
.field{height:36px;background:#f4f5f5;border:1px solid var(--line);border-radius:6px;font-size:11px;color:var(--muted);padding:10px 12px;margin-bottom:17px}
.field.msg{height:86px}
.send{height:34px;width:100%;justify-content:center;position:relative;padding:0}
.send .arrow{position:absolute;right:6px;top:5px}

/* footer */
.footer{top:5030px;left:0;width:1200px;height:346px;background:var(--green);color:var(--white)}
.f-logo{top:5094px;left:150px;font-size:32px}
.f-logo .dot{width:40px;height:40px}
.f-about{top:5162px;left:150px;width:300px;font-size:10px;line-height:22px}
.f-soc{top:5230px;left:150px;display:flex;gap:8px}
.f-soc i{width:22px;height:22px;border-radius:50%;background:var(--white)}
.f-col{top:5092px}
.f-col h4{font-family:"Oswald",sans-serif;font-weight:400;font-size:18px;margin-bottom:24px}
.f-col li{list-style:none;font-size:10px;margin-bottom:12px;display:flex;gap:8px;align-items:center}
.f-rule{top:5292px;left:150px;width:900px;height:1px;background:rgba(255,255,255,.35)}
.f-bottom{top:5318px;left:150px;width:900px;display:flex;justify-content:space-between;font-size:8.5px}
.f-bottom span+span{margin-left:50px}
</style>
</head>
<body>

<!-- header + hero -->
<section class="abs hero" role="img" aria-label="Green semi truck driving on a forest highway"></section>
<div class="abs topbar">
  <div>Follow Us Social Media <span class="soc"><i></i><i></i><i></i></span></div>
  <div>Sign In &nbsp; Register</div>
</div>
<nav class="abs nav">
  <div class="logo"><span class="dot"></span>CargoLoop</div>
  <div class="menu"><span>HOME</span><span>ABOUT US</span><span>FOR TRUCKING COMPANIES</span><span>FOR DRIVERS</span></div>
  <span class="btn">Contact Us <span class="arrow"><svg width="10" height="10" viewBox="0 0 10 10"><path d="M2 8 8 2M3 2h5v5" stroke="#0f7a57" stroke-width="1.5" fill="none"/></svg></span></span>
</nav>
<div class="abs hero-title">
  <div class="l1">ON DEMAND</div>
  <div class="l2">Professional Drivers</div>
  <div class="l3">You Can Trust</div>
</div>
<div class="abs search">Enter Job Title Or Skill <span class="go"><svg width="12" height="12" viewBox="0 0 12 12"><circle cx="5" cy="5" r="3.5" stroke="#1c1f22" stroke-width="1.5" fill="none"/><path d="M8 8l3 3" stroke="#1c1f22" stroke-width="1.5"/></svg></span></div>
<span class="abs btn find">Find Drivers <span class="arrow"><svg width="11" height="11" viewBox="0 0 12 12"><circle cx="5" cy="5" r="3.5" stroke="#0f7a57" stroke-width="1.5" fill="none"/><path d="M8 8l3 3" stroke="#0f7a57" stroke-width="1.5"/></svg></span></span>
<div class="abs rating"><span class="name">Reviewly</span><span><small>4.9/5.0 Rating</small><span class="stars">★★★★★</span></span></div>
<div class="abs hero-card">
  <div class="row">On-Demand, Qualified Drivers <span>›</span></div>
  <div class="row">Real Standards, Real Results <span>›</span></div>
  <div class="row">Connecting Companies &amp; Drivers <span>›</span></div>
  <p>CargoLoop bridges the gap between companies needing drivers and drivers seeking steady work on the road.</p>
</div>

<!-- about -->
<div class="abs photo about-photo" role="img" aria-label="Truck driver with cap standing in front of blue trucks"></div>
<div class="abs badge"><b>24+</b><span>Years Of Experience</span></div>
<div class="abs about-text">
  <div class="eyebrow">- About Us</div>
  <h2>Your Partner For Reliable Drivers</h2>
  <p class="para">CargoLoop Connects Trucking Companies With Qualified, Professional Contract Drivers Exactly When And Where You Need Them. Whether You're A Fleet Manager Looking For Drivers Or A Professional Driver Ready For Your Next Opportunity, CargoLoop Keeps You Moving.</p>
  <ul class="ticks">
    <li><svg width="12" height="10"><path d="M1 5l3.5 3.5L11 1" stroke="#0f7a57" stroke-width="1.8" fill="none"/></svg>Lorem Ipsum Dolor Sit Amet Consectetur. Accumsan In Convallis Ac Est In.</li>
    <li><svg width="12" height="10"><path d="M1 5l3.5 3.5L11 1" stroke="#0f7a57" stroke-width="1.8" fill="none"/></svg>Lorem Ipsum Dolor Sit Amet Consectetur. Vel Sed Adipiscing Egestas Mi. Odio.</li>
    <li><svg width="12" height="10"><path d="M1 5l3.5 3.5L11 1" stroke="#0f7a57" stroke-width="1.8" fill="none"/></svg>Lorem Ipsum Dolor Sit Amet Consectetur. Facilisis Elementum Urna Non.</li>
  </ul>
  <span class="btn">Learn More About Us <span class="arrow"><svg width="10" height="10" viewBox="0 0 10 10"><path d="M2 8 8 2M3 2h5v5" stroke="#0f7a57" stroke-width="1.5" fill="none"/></svg></span></span>
</div>

<!-- go-to -->
<div class="abs goto">
  <h2>Your Go-To People For Hiring Truck Drivers</h2>
  <p class="para">Lorem Ipsum Dolor Sit Amet Consectetur. Nulla Diam Nam Sem Et Lobortis Aliquam. Neque Ac Suspendisse Mi Ut Dictum Sagittis Sit Suspendisse Nulla. Mattis A Sed Sodales Dui In Tempus. Vehicula Laoreet Etiam Ut Tincidunt Aliquam Pellentesque Nunc. Et Non Habitasse In Porttitor Arcu. Vestibulum Sed Suscipit Vitae Scelerisque Tristique. Lectus Consectetur Scelerisque Auctor Pretium Eget Nunc Vulputate Volutpat Auctor.</p>
  <p class="para" style="margin-top:8px">Sem Cras Elit Faucibus Quam Augue Amet. Eu Quam Faucibus Mauris Id Egestas Morbi Sagittis Dui Augue. Eget Pellentesque Amet Porttitor Sagittis Urna. Vestibulum Nascetur Venenatis Risus Id Lorem Elit Elit In Ipsum. Felis Facilisi Non Augue Purus.</p>
  <span class="btn">Request Drivers <span class="arrow"><svg width="10" height="10" viewBox="0 0 10 10"><path d="M2 8 8 2M3 2h5v5" stroke="#0f7a57" stroke-width="1.5" fill="none"/></svg></span></span>
</div>
<div class="abs photo goto-photo" role="img" aria-label="Smiling driver holding a tablet in a truck yard"></div>
<div class="abs driver-card">
  <div class="who"><i></i>Marcus Hale</div>
  <p>(229) 555-0148<br>Dana.Price@Example.Com</p>
  <p style="color:var(--ink);font-weight:600;margin-top:8px">About The Driver</p>
  <small>Lorem Ipsum Dolor Sit Amet Consectetur Nulla Diam Nam Sem Et Lobortis Aliquam.</small>
</div>
<div class="abs stats">
  <div class="stat"><b>20k+</b><span>Lorem Ipsum Dolor Sit Amet Consectetur. Nulla Mauris Quis Nisi Turpis Aliquam Enim.</span></div>
  <div class="stat"><b>20k+</b><span>Lorem Ipsum Dolor Sit Amet Consectetur. Nulla Mauris Quis Nisi Turpis Aliquam Enim.</span></div>
  <div class="stat"><b>20k+</b><span>Lorem Ipsum Dolor Sit Amet Consectetur. Nulla Mauris Quis Nisi Turpis Aliquam Enim.</span></div>
</div>
<div class="abs trucks" role="img" aria-label="Row of parked semi truck cabs seen from the front"></div>

<!-- why -->
<div class="abs why-photo" role="img" aria-label="White semi truck with trailer on a highway"></div>
<div class="abs why-box">
  <h2>Why Companies &amp; Drivers Trust CargoLoop</h2>
  <ul class="ticks">
    <li><svg width="14" height="11"><path d="M1 5.5l4 4L13 1" stroke="#0f7a57" stroke-width="1.8" fill="none"/></svg>Qualified, Vetted Drivers</li>
    <li><svg width="14" height="11"><path d="M1 5.5l4 4L13 1" stroke="#0f7a57" stroke-width="1.8" fill="none"/></svg>Flexible Contracts</li>
    <li><svg width="14" height="11"><path d="M1 5.5l4 4L13 1" stroke="#0f7a57" stroke-width="1.8" fill="none"/></svg>24/7 Availability</li>
    <li><svg width="14" height="11"><path d="M1 5.5l4 4L13 1" stroke="#0f7a57" stroke-width="1.8" fill="none"/></svg>Competitive Pay For Drivers</li>
    <li><svg width="14" height="11"><path d="M1 5.5l4 4L13 1" stroke="#0f7a57" stroke-width="1.8" fill="none"/></svg>Reliable Service For Companies</li>
  </ul>
  <div class="btns">
    <span class="btn">Request Drivers Today <span class="arrow"><svg width="10" height="10" viewBox="0 0 10 10"><path d="M2 8 8 2M3 2h5v5" stroke="#0f7a57" stroke-width="1.5" fill="none"/></svg></span></span>
    <span class="btn">Join Our Driver Team <span class="arrow"><svg width="10" height="10" viewBox="0 0 10 10"><path d="M2 8 8 2M3 2h5v5" stroke="#0f7a57" stroke-width="1.5" fill="none"/></svg></span></span>
  </div>
</div>

<!-- how -->
<div class="abs how-head"><div class="eyebrow">- How It Works</div><h2>How CargoLoop Works</h2></div>
<svg class="abs" style="top:2990px;left:300px" width="600" height="200" viewBox="0 0 600 200">
  <path d="M100 160 Q170 200 250 150" stroke="#9aa2a7" stroke-dasharray="4 4" fill="none"/>
  <path d="M360 40 Q430 -10 510 40" stroke="#9aa2a7" stroke-dasharray="4 4" fill="none"/>
</svg>
<div class="abs step" style="left:186px">
  <div class="circ" role="img" aria-label="Driver standing beside a white truck" style="background:linear-gradient(160deg,#dfe5ea,#8d9aa3)"></div>
  <h3>For Companies<br>Tell Us What Drivers You Need</h3>
  <p>We Provide Pre-Screened, Professional Drivers To Meet Your Short Or Long-Term Needs.</p>
</div>
<div class="abs step" style="left:449px">
  <div class="circ" role="img" aria-label="Two drivers shaking hands in front of a red truck" style="background:linear-gradient(160deg,#c8303a,#2a5a9a)"></div>
  <h3>For Drivers<br>Join Our Team.</h3>
  <p>Apply Once, Drive When You Want, Get Paid On Time – Every Time.</p>
</div>
<div class="abs step" style="left:712px">
  <div class="circ" role="img" aria-label="Driver checking a truck engine" style="background:linear-gradient(160deg,#dfe4e8,#6f88a4)"></div>
  <h3>CargoLoop Difference<br>Quality You Can Count On.</h3>
  <p>We Uphold Real Standards For Real Results, Keeping Your Business On The Road.</p>
</div>

<!-- cta -->
<div class="abs cta"></div>
<div class="abs cta-truck" role="img" aria-label="Green box truck shown from the side"></div>
<h2 class="abs cta h2" style="all:unset;position:absolute;top:3490px;left:176px;font-family:'Oswald',sans-serif;font-size:44px;color:#fff">Ready To Get Started?</h2>
<div class="abs cta-btns">
  <span class="btn">Find Drivers <span class="arrow"><svg width="10" height="10" viewBox="0 0 10 10"><path d="M2 8 8 2M3 2h5v5" stroke="#0f7a57" stroke-width="1.5" fill="none"/></svg></span></span>
  <span class="btn">Apply To Drive <span class="arrow"><svg width="10" height="10" viewBox="0 0 10 10"><path d="M2 8 8 2M3 2h5v5" stroke="#0f7a57" stroke-width="1.5" fill="none"/></svg></span></span>
</div>

<!-- testimonials -->
<h2 class="abs testi-head">What Our Clients &amp; Drivers Say</h2>
<div class="abs avatar" role="img" aria-label="Portrait of a transport manager"></div>
<p class="abs testi-text">Lorem Ipsum Dolor Sit Amet Consectetur. Blandit Lacinia Diam Magna Phasellus Habitant Cras Et Pellentesque Commodo. Consectetur Ultrices Sed Nulla Pellentesque. Augue Sed Sit Odio Placerat Eleifend Id Facilisi. Integer Eget Ac Tortor In Dui Et Quam. Non Fringilla Volutpat Elementum Neque Bibendum. Nulla Fermentum Accumsan Et Vitae Suscipit Ut Nisl Dapibus Bibendum. Donec Urna Tellus Elementum Quam.</p>
<div class="abs testi-name">Marcus Hale<br><span style="color:var(--muted)">Transport Manager</span></div>
<div class="abs arrows">
  <span><svg width="16" height="12"><path d="M15 6H2M6 1 1 6l5 5" stroke="#1c1f22" stroke-width="1.5" fill="none"/></svg></span>
  <span><svg width="16" height="12"><path d="M1 6h13M10 1l5 5-5 5" stroke="#1c1f22" stroke-width="1.5" fill="none"/></svg></span>
</div>
<div class="abs brands">
  <span>Northway</span><span>Baymart</span><span>Crestline</span><span>Quikkart</span><span>Valemart</span><span><i></i>Pinnacle</span>
</div>

<!-- contact -->
<div class="abs map" role="img" aria-label="Light grey world map with location pins"></div>
<svg class="abs pin" style="top:4442px;left:450px" viewBox="0 0 22 28"><path d="M11 27C4 18 1 14 1 10a10 10 0 0 1 20 0c0 4-3 8-10 17z" fill="#0f7a57"/><circle cx="11" cy="10" r="4" fill="#fff"/></svg>
<svg class="abs pin" style="top:4618px;left:136px" viewBox="0 0 22 28"><path d="M11 27C4 18 1 14 1 10a10 10 0 0 1 20 0c0 4-3 8-10 17z" fill="#0f7a57"/><circle cx="11" cy="10" r="4" fill="#fff"/></svg>
<svg class="abs pin" style="top:4760px;left:268px" viewBox="0 0 22 28"><path d="M11 27C4 18 1 14 1 10a10 10 0 0 1 20 0c0 4-3 8-10 17z" fill="#0f7a57"/><circle cx="11" cy="10" r="4" fill="#fff"/></svg>
<div class="abs contact">
  <h2>Questions? Let’s Talk.</h2>
  <div class="info">
    <div><svg width="12" height="14" viewBox="0 0 12 14"><path d="M6 13C2 8 1 6.5 1 5a5 5 0 0 1 10 0c0 1.5-1 3-5 8z" stroke="#0f7a57" fill="none" stroke-width="1.3"/></svg>48 Harbor Freight Way, Dayton 45402</div>
    <div><svg width="12" height="12" viewBox="0 0 12 12"><path d="M2 1h3l1 3-2 1a7 7 0 0 0 3 3l1-2 3 1v3c-6 0-10-4-10-9z" stroke="#0f7a57" fill="none" stroke-width="1.2"/></svg>(671) 555-0172</div>
    <div><svg width="13" height="10" viewBox="0 0 13 10"><rect x=".6" y=".6" width="11.8" height="8.8" rx="1" stroke="#0f7a57" fill="none" stroke-width="1.2"/><path d="M1 1l5.5 4L12 1" stroke="#0f7a57" fill="none" stroke-width="1.2"/></svg>Nora.Bell@Example.Com</div>
  </div>
  <div class="field">Name</div>
  <div class="field">E-Mail</div>
  <div class="field">Number</div>
  <div class="field msg">Message</div>
  <span class="btn send">Send Us A Message <span class="arrow"><svg width="10" height="10" viewBox="0 0 10 10"><path d="M2 8 8 2M3 2h5v5" stroke="#0f7a57" stroke-width="1.5" fill="none"/></svg></span></span>
</div>

<!-- footer -->
<footer class="abs footer"></footer>
<div class="abs logo f-logo"><span class="dot"></span>CargoLoop</div>
<p class="abs f-about" style="color:#fff">Lorem Ipsum Dolor Sit Amet Consectetur Ante Viverra Non Fermentum Amet Sagittis Enim Facilisis</p>
<div class="abs f-soc"><i></i><i></i><i></i></div>
<div class="abs f-col" style="left:528px;color:#fff"><h4>Links Used</h4><ul><li>Heim</li><li>Über Mich</li><li>Kontaktieren Sie Uns</li></ul></div>
<div class="abs f-col" style="left:710px;color:#fff"><h4>About</h4><ul><li>Our Story</li><li>Our Mission</li><li>Our Vision</li></ul></div>
<div class="abs f-col" style="left:847px;color:#fff"><h4>Contact Information</h4><ul>
  <li><svg width="10" height="12" viewBox="0 0 12 14"><path d="M6 13C2 8 1 6.5 1 5a5 5 0 0 1 10 0c0 1.5-1 3-5 8z" stroke="#fff" fill="none" stroke-width="1.3"/></svg>48 Harbor Freight Way</li>
  <li><svg width="10" height="10" viewBox="0 0 12 12"><path d="M2 1h3l1 3-2 1a7 7 0 0 0 3 3l1-2 3 1v3c-6 0-10-4-10-9z" stroke="#fff" fill="none" stroke-width="1.2"/></svg>(671) 555-0172</li>
  <li><svg width="11" height="9" viewBox="0 0 13 10"><rect x=".6" y=".6" width="11.8" height="8.8" rx="1" stroke="#fff" fill="none" stroke-width="1.2"/><path d="M1 1l5.5 4L12 1" stroke="#fff" fill="none" stroke-width="1.2"/></svg>Nora.Bell@Example.Com</li>
</ul></div>
<div class="abs f-rule"></div>
<div class="abs f-bottom" style="color:#fff"><span>Copyright © 2025- All Rights Reserved</span><span><span>Terms Of Use</span><span>Privacy Policy</span></span></div>

</body>
</html>
```